Web Design with a Twist! Not cheap design

Please note that this project is ending at 5pm on Tuesday the 28th of September, Australian Western Standard Time!!

Please also note that this project has now been guaranteed!

This project involves three primary elements:
* Logo design;
* Web design - of additional pages and page elements to fit into a site that is already in design/development;
* Graphic design - various images used on the site.

The following materials are included for the project:
* Project requirements
* Company / Site name
* Company / Site description
* Wireframes for new pages / page elements
* Screenshots of existing designs and accompanying definition of constraints for new designs
* PSDs for existing site designs
* Technical requirements for designs
* Content (to guide designs)

Project Requirements:

* Logo design:
This is a new company / site, so we need a new logo. We want to see what you come up with here without giving too much direction that may restrict creativity. If desired, you may find possible guidance through considering the company name, company description, and the existing site designs. Please note that the current logo in the site is for placeholder purposes only.

* Web design:
We need the following pages (and features) to be designed for the site:
• Home page
• Advertise page
• How it works page
We’ve provided some wireframes for the pages, however we definitely don't want you to be guided by the layout/styling at all - the wireframes are only there to indicate the features that we require on each page only. So please ignore all aspects of the wireframes except for the indications of features and functionality.

* Graphic design:
We need various images to be designed throughout the site. These include:
• The image at the top of the ‘Home’ page – please note we will provide some direction on this asap
• The image at the top of the ‘Advertise’ page – please note we will provide some direction n this asap
• The image at the top of the ‘How it Works’ pages
• The images that accompany each of the left hand menu items on the ‘How it Works’ pages (the main images & thumbnails if that’s part of your design). Please note that these images need to be constructed to match the Headlines for each of the ‘What’, ‘Who’, ‘Where’, etc menu items. These Headlines (and some descriptive text) can be found in the Content section at the end of this brief.
• The map of Australia for the ‘Home’ page
• The images to accompany the pricing section of the ‘Advertise’ page
• The variations of the ‘Life in the search lane’ images that are used on the ‘Home’, ‘Advertise’, and ‘How it Works’ pages. Please note that if you want to use different imagery (or no imagery, dependent upon your design) for the Home and Advertise pages then this is your call.

Company Name:
TaskBloom

Company / Site description:
This site will provide a means for contractors ('advertisers') to easily specify and advertise their services, coupled with a means for employers (‘buyers’) to easily seek out and contact these people.
The site will cater for contractor-side advertisements only; job postings will not be accommodated (turning the traditional job advertisement model on its head).
In general, the functionality of the site is somewhat like a mashup of sites like crewvault.com and stayvane.com. The site will incorporate the following primary features of contractor profile display and search, company profile display, (and an availability calendar for v2 release).

Constraints for designs:
On some of the existing designs you will notice that a number of the elements of the site have already been designed. When constructing your designs, please work in accordance with the following constraints:

You have to keep:
• Colour scheme in the header
• Colour scheme in the top navigation buttons (including text colour and background colour)
• Colour scheme for the buttons like on the Register page

You can ignore:
• The existing placeholder logo
• Border, layout, and colour scheme for page elements (like the lines around and inside the register section on the Register page)
• Design of text fields
• Font colour scheme throughout the site – the orange and grey headlines and body text
• Design and colour scheme of the map of Australia
• The breadcrumbs (whether or not they appear, and their layout, styling, colour scheme etc)
• Dropdown styling (assuming you had to make some; currently not on any pages we’re asking you to do) like on the Browse Profession page
• Profile styling (for the home page featured profiles) like on the Browse Profession page
• Footer styling
• Anything else we haven’t explicitly asked you to keep

Technical requirements for design:
Any site designs in either Layered Photoshop files (PSD's) or Illustrator Drawings (AI). RGB Color. Must fit current site design, we work to 1024 wide screens. Usuable area is defined in site designs that are attached in the Photoshop documents; it's around 960px.
Logo work needs to be Illustrator Drawings (AI) and EPS. Need CMYK images for printing and RGB for screen. Logos must include any special fonts that are used as TTF or Open Type. Logos need Color, Monochrome, Reversed and both Tall and Wide usages.

Content for the 'How it Works' pages - this content should guide the images that appear on each page.
* What
Headline: TaskBloom brings contractors and employers together
Descriptive text: (turns the traditional job search model on its head)
* Who
Headline: TaskBloom is for highly skilled professionals and fast moving companies
Descriptive text:
* Where
Headline: Anywhere in Australia, TaskBloom is working by your side
Descriptive text:
* Why
Headline: There are more than 1 million reasons to love TaskBloom
Descriptive text: In Australia, there are 1 million people who work as contractors in their main job, and a further 100,000 people who are contractors in their second job. That’s a lot of contractors!
* When
Headline: TaskBloom is forming partnerships 24 hours a day
Descriptive text:
* How
Headline: Life in the search lane, with TaskBloom
Descriptive text: Advertise on TaskBloom now, and get your life in the search lane.

Remember
Just remember the wireframes we have submitted are just a guide – we want to see your creativity shine. And above all else - have fun!
Thank you.
Updates

Please note the deadline for this design competition 5pm on Tuesday the 28th of September, Australian Western Standard Time.

Just under 3 days away!

The deadline of the project will soon be updated to reflect this.

Hi Designers!

Just to be 100% clear about the deadline - the timer is currently showing 7 hours too many. In other words, the project will end 7 hours before the timer finishes.

I will send a notification if the timer starts to display the correct time. So until then, please remember that the deadline is earlier than it seems!

Thanks

Hi Designers,

A couple of really important points:

Firstly - if everyone could please stick to the theme that we provided in the Photoshop files that would be excellent. It is not possible for us to create a new theme. We're dealing with very tight deadlines, so please just provide designs that fit within the current theme.

Secondly, we were really hoping for more illustrations / graphics to be provided in the designs. We're not a fan of the stock photos of generic business people. So please send through designs that incorporate illustrations / graphics for any imagery.

Also just a reminder that this competition is still ending 7 hours earlier than the timer currently displays.

Thanks.

Target Market(s)

The ‘advertiser’ target market for the site is white collar professionals, in all types of industries. The site will be catering for premium contractors only. The site will be catering for both 'in person' contractors, as well as 'knowledge economy' contractors. The site will not be seeking to compete with gigmora.com, plixo.com, taskrune.com, or similar sites.

The advertiser target market will also encompass companies and labour hire agencies that have contractors in their workforce.

The ‘buyer’ target market will encompass employers, recruitment agents, and member-to-member hiring.

Industry/Entity Type

Contractor

Requirements
Must have
• As per overview
Nice to have
• As per overview
Should not have
• As per overview

```html
<!DOCTYPE html>
<html lang="en">
<head>
<meta charset="utf-8">
<title>TaskBloom – How it Works</title>
<link rel="stylesheet" href="https://fonts.googleapis.com/css2?family=Arimo:wght@400;700&display=swap">
<style>
:root{
  --header-top:#6b7584;
  --header-bottom:#4f5a69;
  --brand-red:#c8102e;
  --tab-grey-top:#b9bcc1;
  --tab-grey-bottom:#8d9198;
  --tab-red-top:#e0182c;
  --tab-red-bottom:#a90d1c;
  --banner-orange:#f06c00;
  --banner-line:#2d6fa6;
  --side-blue-top:#2f8fca;
  --side-blue-bottom:#1f6fa6;
  --side-border:#123f5c;
  --cta-orange-top:#ffa04a;
  --cta-orange-bottom:#f27415;
  --cta-red-top:#d91a2c;
  --cta-red-bottom:#a50c1a;
  --heading-grey:#555a60;
  --body-grey:#555;
  --accent-orange:#ec6a00;
  --footer-grey:#6b6b6b;
  --footer-text:#bdbdbd;
  --white:#fff;
}
*{box-sizing:border-box;margin:0;padding:0}
html,body{width:1200px;height:1172px;overflow:hidden;background:var(--white)}
body{position:relative;font-family:"Arimo",Arial,sans-serif;color:var(--body-grey)}

.site-header{position:absolute;left:0;top:0;width:1200px;height:157px;
  background:linear-gradient(var(--header-top),var(--header-bottom))}
.brand{position:absolute;left:143px;top:36px;display:flex;align-items:center;gap:10px;
  font-size:50px;font-weight:700;color:var(--brand-red);letter-spacing:-1px}
.brand-dot{width:14px;height:14px;border-radius:50%;background:var(--brand-red)}
.utility-links{position:absolute;left:857px;top:27px;font-size:13px;color:#e8ebef;display:flex;gap:14px}
.utility-links .sep{color:#aab2bd}

.main-nav{position:absolute;top:125px;left:0;height:32px}
.main-nav a{position:absolute;top:0;height:32px;border-radius:6px 6px 0 0;
  background:linear-gradient(var(--tab-grey-top),var(--tab-grey-bottom));
  color:var(--white);font-size:15px;font-weight:700;text-decoration:none;
  display:flex;align-items:center;justify-content:center;text-shadow:0 1px 1px rgba(0,0,0,.35)}
.main-nav a.is-active{background:linear-gradient(var(--tab-red-top),var(--tab-red-bottom))}

.hero{position:absolute;left:0;top:157px;width:1200px;height:226px;background:var(--banner-orange);
  border-bottom:5px solid var(--banner-line);height:231px}
.hero-photo{position:absolute;bottom:5px;border-radius:90px 90px 0 0;
  background:linear-gradient(#e9b48a,#3a3a3c 70%)}
.hero-photo.left{left:188px;width:232px;height:222px}
.hero-photo.right{left:764px;width:239px;height:222px}
.hero-copy{position:absolute;left:400px;top:20px;width:380px;text-align:center;color:var(--white)}
.hero-title{font-size:35px;line-height:43px;font-weight:700;text-shadow:0 2px 6px rgba(0,0,0,.55)}
.hero-sub{font-size:20px;line-height:35px;margin-top:2px;text-shadow:0 1px 3px rgba(0,0,0,.4)}

.side-menu{position:absolute;left:186px;top:428px;width:215px;height:512px;border-radius:8px;
  border:2px solid var(--side-border);
  background:linear-gradient(90deg,var(--side-blue-bottom),var(--side-blue-top) 60%,#47a6dc)}
.side-menu h2{position:absolute;left:19px;top:14px;font-size:23px;color:var(--white);font-weight:700}
.side-menu ul{list-style:none;position:absolute;left:0;top:54px;width:100%}
.side-menu li{height:63px;border-top:1px solid rgba(255,255,255,.22);display:flex;align-items:center;
  padding-left:14px;gap:26px;color:var(--white);font-size:16px;font-weight:700}
.menu-icon{width:44px;height:44px;border-radius:50%;background:radial-gradient(#2d7fc0,#0f4f86)}
.side-cta{position:absolute;left:24px;top:445px;width:168px;height:51px;border-radius:4px;
  border:2px solid #ffd2a6;background:linear-gradient(var(--cta-orange-top),var(--cta-orange-bottom));
  color:var(--white);font-size:22px;font-weight:700;display:flex;align-items:center;justify-content:center}

.welcome{position:absolute;left:436px;top:426px;width:540px}
.welcome h1{font-size:34px;font-weight:700;color:var(--heading-grey);letter-spacing:-.5px;line-height:40px}
.welcome p{font-size:13px;line-height:21px;margin-top:2px}

.feature-box{position:absolute;left:429px;top:714px;width:522px;height:229px;border-radius:8px;
  border:1px solid #dcdfe3;background:radial-gradient(ellipse at 40% 40%,#fff,#eef0f3);
  box-shadow:0 0 6px rgba(0,0,0,.12)}
.feature-box h3{position:absolute;left:23px;top:25px;font-size:22px;color:var(--accent-orange);font-weight:700;
  padding-bottom:6px;border-bottom:1px solid #e2e2e2;width:440px}
.feature-box p{position:absolute;left:23px;top:60px;width:460px;font-size:13px;line-height:21px}
.contractor-select{position:absolute;left:13px;top:182px;width:257px;height:31px;border:1px solid #cfd2d6;
  background:var(--white);border-radius:3px;font-size:18px;color:#b2b5b9;display:flex;align-items:center;padding-left:42px}
.contractor-select .caret{position:absolute;right:0;top:0;width:31px;height:29px;border-left:1px solid #cfd2d6;
  display:flex;align-items:center;justify-content:center}
.box-cta{position:absolute;left:295px;top:182px;width:208px;height:31px;border-radius:3px;
  background:linear-gradient(var(--cta-red-top),var(--cta-red-bottom));color:var(--white);
  font-size:18px;font-weight:700;display:flex;align-items:center;justify-content:center}

.site-footer{position:absolute;left:0;top:1025px;width:1200px;height:147px;
  background:repeating-linear-gradient(45deg,#707070 0 2px,var(--footer-grey) 2px 4px)}
.footer-col{position:absolute;top:17px;font-size:12px;line-height:16px;color:var(--footer-text)}
.footer-col strong{display:block;color:#cfcfcf}
.copyright{position:absolute;left:830px;top:17px;font-size:12px;font-weight:700;color:#cfcfcf}
.social{position:absolute;left:840px;top:50px;display:flex;gap:12px}
.social span{width:26px;height:26px;border-radius:4px;background:#4a79a8}
</style>
</head>
<body>
<header class="site-header">
  <div class="brand"><span class="brand-dot"></span>TaskBloom</div>
  <nav class="utility-links"><span>Contact Us</span><span class="sep">|</span><span>Site Map</span></nav>
  <nav class="main-nav">
    <a style="left:360px;width:74px">Home</a>
    <a style="left:438px;width:99px">Find</a>
    <a style="left:540px;width:93px">Advertise</a>
    <a class="is-active" style="left:635px;width:109px">How it works</a>
    <a style="left:747px;width:98px">Blog</a>
    <a style="left:849px;width:98px">Login</a>
  </nav>
</header>

<section class="hero">
  <div class="hero-photo left" role="img" aria-label="Photo of a smiling businesswoman"></div>
  <div class="hero-copy">
    <div class="hero-title">Experienced<br>profrssionals<br>working for you.</div>
    <div class="hero-sub">Aliquipit nis nis ad eriuscil utem<br>vent prationsed el</div>
  </div>
  <div class="hero-photo right" role="img" aria-label="Photo of a smiling senior businessman in a suit"></div>
</section>

<aside class="side-menu">
  <h2>How it Works</h2>
  <ul>
    <li><span class="menu-icon" role="img" aria-label="Question mark illustration"></span>What</li>
    <li><span class="menu-icon" role="img" aria-label="Puzzle piece illustration"></span>Who</li>
    <li><span class="menu-icon" role="img" aria-label="Crossed arrows illustration"></span>Where</li>
    <li><span class="menu-icon" role="img" aria-label="Cube illustration"></span>Why</li>
    <li><span class="menu-icon" role="img" aria-label="Clock illustration"></span>When</li>
    <li><span class="menu-icon" role="img" aria-label="Light bulb illustration"></span>How</li>
  </ul>
  <div class="side-cta">Advertise</div>
</aside>

<main class="welcome">
  <h1>Welcome</h1>
  <p>Nostion vulputat. Ip ea feugiatem nulput lum ad tem diam voluptat atismod ignisi endionse eui tie molobor periurem dolore veliquamet aliquis adipis nonsectem ese diam iustis er alisl exerit laor sit vulputet, quamet lor acipsuscidulaor sit vulputet, quamet lor acipsuscidui exer iure et amet, sustis essequi enit incilit venim del ex et amet, con heniat nim quatum eum euip etum nulla facilit, sit, quisim dolorpe rostio con velesecte dolorpe rating et lorer si exer ad dolorerci ex eui tat at. Ut vulla consectem delit alis eu faccum ipit velenibh er irit lutat. Aliquam quatet, se dit lute min euis adit inisi te dolore i exer iure et amet, sustis essequi enit incilit venim del ex et amet, con heniat nim quatum eum euip etum nulla facilit, sit, quisim dolorpe rostio con velesecte dolorpe rating et lorer si exer ad dolorerci ex eui tat at. Ut vulla consectem delit alis eu faccum ipit velenibh er irit lutat. Aliquam quatet, se dit lute min euis adit inisi te dolore dolobor senis digna feuisi blandre tionsectem nim ilit at wis aliquipisi.</p>
</main>

<section class="feature-box">
  <h3>Headline</h3>
  <p>Reuip etum nulla facilit, sit, quisim dolorpe rostio con velesecte dolorpe rating et lorer si exer ad dolorerci ex eui tat at. Ut vulla consectem delit alis eu faccum ipit velenibh er irit lutat. Aliquam quatet, se dit lute min euis adit inisi te dolore dolobor senis digna feuisi blandre tionsectem nim ilit at wis aliquipisi.</p>
  <div class="contractor-select">Find contractors
    <span class="caret"><svg width="10" height="6" viewBox="0 0 10 6"><path d="M0 0h10L5 6z" fill="#777"/></svg></span>
  </div>
  <div class="box-cta">Advertise</div>
</section>

<footer class="site-footer">
  <div class="footer-col" style="left:240px"><strong>The Service</strong>About<br>Browse<br>Log In</div>
  <div class="footer-col" style="left:393px"><strong>Support</strong>Contact Us<br>FAQ</div>
  <div class="footer-col" style="left:537px"><strong>Legal</strong>Privacy Policy<br>Terms &amp; Conditions</div>
  <div class="copyright">2010 WorkLoom Pty Ltd</div>
  <div class="social" aria-label="Social links">
    <span></span><span></span><span></span><span style="background:#d9782f"></span>
  </div>
</footer>
</body>
</html>
```